Volta Medica Innovative Business Card

Stunning business card. Background will be black. Letters in gold. Modern yet simple design that is attention grabbing. QR code leading to site. Attractive primarily to males ages 30 to 50 but also to females in same age range looking for beauty and mental health products

Target Market(s)

Males in the 30-50 age demographics

Industry/Entity Type

Pharmaceuticals selling erectile dysfunction and mens health medications

Contact Information for Business Card

www.voltamedica.example; (555) NOW-BOLT; info@voltamedica.example

Colors
FFC000
F8CF3A
FAE287
FDF2CF
FEFAEE

Requirements
Must have
• Black business card with gold letters.
Nice to have
• perhaps just the logo or the "R" icon by itself on one side
Should not have
• too much content so it does not look busy

```html
<!DOCTYPE html>
<html lang="en">
<head>
<meta charset="utf-8">
<title>Volta Medica Business Card</title>
<link rel="stylesheet" href="https://fonts.googleapis.com/css2?family=Arimo:wght@400;700&display=swap">
<style>
  :root {
    --page-bg: #141414;
    --card-bg: #2a2a2a;
    --gold: #d9a92e;
    --gold-light: #f8cf3a;
    --gold-edge: #b8892a;
    --text-light: #f2f2f2;
    --rule: #e8e8e8;
  }
  * { margin: 0; padding: 0; box-sizing: border-box; }
  html, body {
    width: 1200px; height: 963px; overflow: hidden;
    background: var(--page-bg);
    font-family: "Arimo", Arial, sans-serif;
  }
  .stage {
    width: 1200px; height: 963px;
    display: flex; flex-direction: column; align-items: center; justify-content: center;
    gap: 40px;
  }
  .card {
    position: relative;
    width: 700px; height: 400px;
    background: var(--card-bg);
    border-radius: 22px;
    border-bottom: 3px solid var(--gold-edge);
    overflow: hidden;
  }
  .brand {
    position: absolute;
    display: flex; align-items: center; gap: 16px;
    white-space: nowrap;
  }
  .brand-dot { flex: none; border-radius: 50%; background: var(--gold); }
  .brand-name { font-weight: 700; color: var(--gold); letter-spacing: 2px; }

  .card-back .brand { left: 0; right: 0; top: 165px; justify-content: center; }
  .card-back .brand-dot { width: 40px; height: 40px; }
  .card-back .brand-name { font-size: 56px; }

  .holder { position: absolute; left: 50px; top: 62px; }
  .holder-name {
    font-size: 26px; font-weight: 700; color: var(--gold-light);
    letter-spacing: 0.5px; text-transform: uppercase;
  }
  .holder-role { font-size: 17px; color: var(--text-light); margin-top: 4px; }
  .divider {
    position: absolute; left: 40px; right: 150px; top: 138px;
    height: 1px; background: var(--rule);
  }
  .contacts { position: absolute; left: 50px; top: 158px; list-style: none; }
  .contacts li {
    display: flex; align-items: center; gap: 12px;
    font-size: 19px; color: var(--text-light); margin-bottom: 10px;
  }
  .contacts svg { width: 18px; height: 18px; flex: none; }

  .card-front .brand { right: 60px; top: 236px; }
  .card-front .brand-dot { width: 26px; height: 26px; }
  .card-front .brand-name { font-size: 36px; }

  .website {
    position: absolute; right: 60px; bottom: 40px;
    display: flex; align-items: center; gap: 12px;
    font-size: 19px; color: var(--text-light);
  }
  .website svg { width: 18px; height: 18px; }
</style>
</head>
<body>
<main class="stage">
  <section class="card card-back" aria-label="Card back">
    <div class="brand">
      <span class="brand-dot"></span>
      <span class="brand-name">VOLTA MEDICA</span>
    </div>
  </section>

  <section class="card card-front" aria-label="Card front">
    <div class="holder">
      <h1 class="holder-name">Marcus Hale</h1>
      <p class="holder-role">Manager</p>
    </div>
    <div class="divider"></div>
    <ul class="contacts">
      <li>
        <svg viewBox="0 0 24 24" aria-hidden="true"><path fill="var(--gold)" d="M6.6 10.8a15 15 0 0 0 6.6 6.6l2.2-2.2a1 1 0 0 1 1-.25 11.4 11.4 0 0 0 3.6.57 1 1 0 0 1 1 1V20a1 1 0 0 1-1 1A17 17 0 0 1 3 4a1 1 0 0 1 1-1h3.5a1 1 0 0 1 1 1c0 1.25.2 2.45.57 3.57a1 1 0 0 1-.25 1z"/></svg>
        (555) NOW-BOLT
      </li>
      <li>
        <svg viewBox="0 0 24 24" aria-hidden="true"><path fill="var(--gold)" d="M2 5h20v14H2z"/><path fill="none" stroke="var(--card-bg)" stroke-width="1.6" d="M2 5l10 8 10-8"/></svg>
        info@voltamedica.example
      </li>
    </ul>
    <div class="brand">
      <span class="brand-dot"></span>
      <span class="brand-name">VOLTA MEDICA</span>
    </div>
    <div class="website">
      <svg viewBox="0 0 24 24" aria-hidden="true"><circle cx="12" cy="12" r="10" fill="var(--gold)"/><path fill="none" stroke="var(--card-bg)" stroke-width="1.4" d="M2 12h20M12 2c3 3 3 17 0 20M12 2c-3 3-3 17 0 20"/></svg>
      www.voltamedica.example
    </div>
  </section>
</main>
</body>
</html>
```